Conceptual Model Diagram for Replacing Medication with Behavior to Support Weight Loss Maintenance

Design a figure of a conceptual model that needs to be inserted into a word document for a PSF grant. This conceptual model illustrates how behavioral strategies can replace the regulatory functions lost after AOM discontinuation. The intervention targets three core vulnerabilities—appetite resurgence, metabolic inflexibility, and suboptimal mindstate—through the domains of Food, Physical Activity, and Mind. Sustained weight loss maintenance occurs at the intersection of these domains. The intervention is delivered within a design framework that makes behaviors easier to perform, aligns them with identity, and reinforces them through virtual support and community, ensuring real-world feasibility and long-term adherence.
Target Market(s)
PSF reviewers
Industry/Entity Type
academic
Other font styles liked:
- arial
Requirements
Must have
- see my attached description

```html
<!DOCTYPE html>
<html lang="en">
<head>
<meta charset="utf-8">
<title>Conceptual Model – Behavior for Weight Loss Maintenance</title>
<link href="https://fonts.googleapis.com/css2?family=Arimo:wght@400;700&display=swap" rel="stylesheet">
<style>
  :root {
    --bg: #ffffff;
    --ink: #111111;
    --ring: #808080;
    --domain-fill: #bcbcbc;
    --domain-edge: #f4f4f4;
    --icon-tone: #9a9a9a;
  }
  html, body {
    margin: 0;
    padding: 0;
    width: 1200px;
    height: 1200px;
    overflow: hidden;
    background: var(--bg);
  }
  .model {
    display: block;
    width: 1200px;
    height: 1200px;
    font-family: "Arimo", Arial, sans-serif;
  }
  .model-title {
    font-weight: 700;
    font-size: 46px;
    fill: var(--ink);
  }
  .frame-circle {
    fill: none;
    stroke: var(--ring);
    stroke-width: 2.5;
  }
  .domain {
    fill: var(--domain-fill);
    fill-opacity: 0.62;
    stroke: var(--domain-edge);
    stroke-width: 2.5;
  }
  .domain-label {
    font-size: 36px;
    fill: var(--ink);
  }
  .core-label {
    font-size: 33px;
    fill: var(--ink);
  }
  .cycle-path,
  .spoke {
    fill: none;
    stroke: var(--ring);
    stroke-width: 3;
  }
  .cycle-label {
    font-size: 33px;
    fill: var(--ink);
  }
  .arrow-head { fill: var(--ring); }
  .icon-slot {
    fill: var(--icon-tone);
    opacity: 0.55;
  }
</style>
</head>
<body>
<svg class="model" viewBox="0 0 1200 1200" xmlns="http://www.w3.org/2000/svg">
  <defs>
    <marker id="arrow" viewBox="0 0 10 10" refX="8" refY="5" markerWidth="7" markerHeight="7" orient="auto-start-reverse" markerUnits="userSpaceOnUse">
      <path class="arrow-head" d="M0,0 L10,5 L0,10 z" transform="scale(1)"/>
    </marker>
    <marker id="arrow-lg" viewBox="0 0 10 10" refX="8" refY="5" markerWidth="22" markerHeight="22" orient="auto" markerUnits="userSpaceOnUse">
      <path class="arrow-head" d="M0,0 L10,5 L0,10 z"/>
    </marker>
  </defs>

  <text class="model-title" x="594" y="66" text-anchor="middle">Conceptal Model</text>

  <!-- Delivery framework cycle -->
  <g class="cycle">
    <path class="cycle-path" d="M279,266 A472,472 0 0 1 507,147"/>
    <path class="cycle-path" d="M686,144 A472,472 0 0 1 932,271" marker-end="url(#arrow-lg)"/>
    <path class="cycle-path" d="M1010,370 A472,472 0 0 1 1052,463"/>
    <path class="cycle-path" d="M1074,584 A472,472 0 0 1 1053,752" marker-end="url(#arrow-lg)"/>
    <path class="cycle-path" d="M957,922 A472,472 0 0 1 857,1006"/>
    <path class="cycle-path" d="M778,1047 A472,472 0 0 1 630,1080"/>
    <path class="cycle-path" d="M567,1080 A472,472 0 0 1 327,992"/>
    <path class="cycle-path" d="M283,956 A472,472 0 0 1 173,804" marker-end="url(#arrow-lg)"/>
    <path class="cycle-path" d="M132,637 A472,472 0 0 1 182,396"/>
  </g>

  <!-- Spokes from the framework ring to vulnerabilities -->
  <g class="spokes">
    <line class="spoke" x1="875" y1="341" x2="937" y2="282" marker-end="url(#arrow-lg)"/>
    <line class="spoke" x1="325" y1="347" x2="263" y2="294" marker-end="url(#arrow-lg)"/>
    <line class="spoke" x1="364" y1="906" x2="310" y2="968" marker-end="url(#arrow-lg)"/>
    <line class="spoke" x1="600" y1="993" x2="600" y2="1078" marker-end="url(#arrow-lg)"/>
    <line class="spoke" x1="831" y1="914" x2="873" y2="964"/>
    <line class="spoke" x1="226" y1="695" x2="181" y2="705"/>
  </g>

  <circle class="frame-circle" cx="603" cy="609" r="373"/>

  <!-- Intervention domains -->
  <g class="domains">
    <circle class="domain" cx="603" cy="488" r="182"/>
    <circle class="domain" cx="491" cy="681" r="184"/>
    <circle class="domain" cx="716" cy="681" r="184"/>
  </g>

  <text class="domain-label" x="603" y="426" text-anchor="middle">Food</text>
  <text class="domain-label" text-anchor="middle">
    <tspan x="431" y="692">Physical</tspan>
    <tspan x="437" y="735">Activity</tspan>
  </text>
  <text class="domain-label" x="773" y="703" text-anchor="middle">Mind</text>
  <text class="core-label" text-anchor="middle">
    <tspan x="597" y="577">Sustained</tspan>
    <tspan x="598" y="617">Weight Loss</tspan>
    <tspan x="605" y="656">Maintnance</tspan>
  </text>

  <!-- Framework and vulnerability labels -->
  <text class="cycle-label" x="617" y="228" text-anchor="middle">Make it Easy</text>
  <text class="cycle-label" text-anchor="middle">
    <tspan x="1027" y="297">Metabolic</tspan>
    <tspan x="1024" y="340">Inflexibility</tspan>
  </text>
  <text class="cycle-label" text-anchor="middle">
    <tspan x="1066" y="513">Align With</tspan>
    <tspan x="1054" y="555">Identity</tspan>
  </text>
  <text class="cycle-label" text-anchor="middle">
    <tspan x="920" y="1043">Virtual Support</tspan>
    <tspan x="945" y="1086">and Social Connection</tspan>
  </text>
  <text class="cycle-label" text-anchor="middle">
    <tspan x="595" y="1117">Suboptimal</tspan>
    <tspan x="598" y="1159">Mindstate</tspan>
  </text>
  <text class="cycle-label" text-anchor="middle">
    <tspan x="250" y="1027">Metabolic</tspan>
    <tspan x="248" y="1069">Inflexibility</tspan>
  </text>
  <text class="cycle-label" text-anchor="middle">
    <tspan x="169" y="325">Appetite</tspan>
    <tspan x="170" y="368">Resurgence</tspan>
  </text>

  <!-- Icon areas -->
  <rect class="icon-slot" x="537" y="94" width="116" height="69" rx="10" role="img" aria-label="Icon of a person with a headset and a cycle arrow, representing easy access"/>
  <rect class="icon-slot" x="956" y="766" width="94" height="143" rx="10" role="img" aria-label="Icon of two people connecting above a circular arrow, representing social support"/>
  <rect class="icon-slot" x="103" y="662" width="72" height="129" rx="10" role="img" aria-label="Icon of a stamp with radiating lines, representing identity"/>
</svg>
</body>
</html>
```